BPR Business Card

We need a business card that reflect our business, we have put anther business card as an example of what we like but please feel free to do your own thing.

Here are the items to be placed on card

Glen Harwick
Bright Parcel Route
Mobile: 917-555-4862
Office: 516-555-7104
Fax: 866-555-3927
Email: info@brightparcelroute.example
Website: brightparcelroute.example

I have added raw files to upload

Glen Harwick
Bright Parcel Route
Mobile: 917-555-4862
Office: 516-555-7104
Fax: 866-555-3927 

Target Market(s)

Natural product manufactures, and retailers and distributors

Industry/Entity Type

Business

Requirements
Must have
• 1. Logo
2. The colors of the company

```html
<!DOCTYPE html>
<html lang="en">
<head>
<meta charset="utf-8">
<title>Bright Parcel Route – Business Card</title>
<link rel="stylesheet" href="https://fonts.googleapis.com/css2?family=Lato:wght@400;700;900&family=Raleway:wght@300&display=swap">
<style>
  :root {
    --brand-green: #6db544;
    --panel-dark: #222222;
    --ink: #1f1f1f;
    --paper: #ffffff;
    --pattern-light: #eef0ec;
    --pattern-mid: #f7f8f5;
  }
  * { margin: 0; padding: 0; box-sizing: border-box; }
  html, body { width: 1200px; height: 720px; overflow: hidden; background: var(--paper); }
  .card {
    position: relative;
    width: 1200px;
    height: 720px;
    overflow: hidden;
    background: var(--paper);
    font-family: "Lato", sans-serif;
  }
  .card__pattern {
    position: absolute; left: 0; top: 0; width: 605px; height: 720px;
    background: linear-gradient(135deg, var(--pattern-light), var(--pattern-mid) 50%, var(--pattern-light));
  }
  .card__green-panel {
    position: absolute; left: 605px; top: 0; width: 595px; height: 720px;
    background: var(--brand-green);
  }
  .card__shapes { position: absolute; left: 0; top: 0; }
  .holder { position: absolute; left: 672px; top: 82px; }
  .holder__name {
    font-family: "Raleway", sans-serif;
    font-weight: 300;
    font-size: 38px;
    letter-spacing: 1.5px;
    color: var(--paper);
    text-transform: uppercase;
    line-height: 1;
  }
  .holder__company {
    margin-top: 14px;
    margin-left: -12px;
    font-size: 29px;
    color: var(--ink);
    line-height: 1;
  }
  .brand {
    position: absolute; left: 60px; top: 390px; width: 540px;
    display: flex; align-items: center; justify-content: center; gap: 16px;
  }
  .brand__mark { width: 34px; height: 34px; background: var(--brand-green); flex: none; }
  .brand__name {
    font-weight: 900;
    font-size: 42px;
    color: var(--brand-green);
    text-transform: uppercase;
    letter-spacing: 0.5px;
    white-space: nowrap;
  }
  .contact {
    position: absolute; left: 728px;
    color: var(--paper);
    font-size: 29px;
    line-height: 1;
    white-space: nowrap;
  }
  .contact--small { font-size: 25px; }
  .contact--mobile { top: 222px; }
  .contact--office { top: 310px; }
  .contact--fax { top: 391px; left: 733px; }
  .contact--email { top: 492px; left: 732px; }
  .contact--web { top: 588px; left: 732px; }
</style>
</head>
<body>
<div class="card">
  <div class="card__pattern" role="img" aria-label="Faint repeated brand name pattern on white"></div>
  <div class="card__green-panel"></div>

  <svg class="card__shapes" width="1200" height="720" viewBox="0 0 1200 720" aria-hidden="true">
    <!-- dark contact panel -->
    <rect x="43" y="196" width="677" height="451" rx="24" fill="var(--panel-dark)"/>
    <!-- green separators between contact tabs -->
    <g fill="var(--brand-green)">
      <rect x="605" y="277" width="115" height="8" rx="4"/>
      <rect x="605" y="366" width="115" height="8" rx="4"/>
      <rect x="605" y="456" width="115" height="8" rx="4"/>
      <rect x="605" y="549" width="115" height="8" rx="4"/>
    </g>
    <!-- icon rings -->
    <g fill="none" stroke="var(--brand-green)" stroke-width="3.5">
      <circle cx="681" cy="237" r="29"/>
      <circle cx="681" cy="325" r="29"/>
      <circle cx="681" cy="416" r="29"/>
      <circle cx="681" cy="505" r="29"/>
      <circle cx="681" cy="606" r="29"/>
    </g>
    <!-- mobile -->
    <g fill="none" stroke="var(--paper)" stroke-width="2.5">
      <rect x="671" y="220" width="20" height="34" rx="3"/>
      <line x1="675" y1="214" x2="675" y2="220"/>
      <rect x="675" y="225" width="12" height="8"/>
    </g>
    <g fill="var(--paper)">
      <rect x="675" y="237" width="3" height="3"/><rect x="680" y="237" width="3" height="3"/><rect x="685" y="237" width="3" height="3"/>
      <rect x="675" y="242" width="3" height="3"/><rect x="680" y="242" width="3" height="3"/><rect x="685" y="242" width="3" height="3"/>
      <rect x="675" y="247" width="3" height="3"/><rect x="680" y="247" width="3" height="3"/><rect x="685" y="247" width="3" height="3"/>
    </g>
    <!-- office phone -->
    <g fill="var(--paper)">
      <path d="M664 320 q17 -12 34 0 l-2 6 h-7 l-1 -4 h-14 l-1 4 h-7 z"/>
      <path d="M670 327 h22 l4 12 h-30 z"/>
    </g>
    <circle cx="681" cy="332" r="3.5" fill="var(--panel-dark)"/>
    <!-- fax -->
    <g fill="none" stroke="var(--paper)" stroke-width="2.2">
      <rect x="671" y="398" width="18" height="16"/>
      <line x1="674" y1="403" x2="686" y2="403"/><line x1="674" y1="408" x2="686" y2="408"/>
      <rect x="665" y="414" width="31" height="18" rx="2"/>
    </g>
    <path d="M672 425 q9 -7 18 0 v3 h-18 z" fill="var(--paper)"/>
    <!-- email -->
    <g fill="none" stroke="var(--paper)" stroke-width="2.5">
      <rect x="664" y="494" width="34" height="23"/>
      <polyline points="664,494 681,508 698,494"/>
    </g>
    <!-- web -->
    <g fill="none" stroke="var(--paper)" stroke-width="2.2">
      <circle cx="681" cy="606" r="17"/>
      <ellipse cx="681" cy="606" rx="7" ry="17"/>
      <line x1="664" y1="606" x2="698" y2="606"/>
      <line x1="667" y1="597" x2="695" y2="597"/>
      <line x1="667" y1="615" x2="695" y2="615"/>
      <line x1="681" y1="589" x2="681" y2="623"/>
    </g>
  </svg>

  <div class="holder">
    <p class="holder__name">Glen Harwick</p>
    <p class="holder__company">Bright Parcel Route</p>
  </div>

  <div class="brand">
    <span class="brand__mark"></span>
    <span class="brand__name">Bright Parcel Route</span>
  </div>

  <p class="contact contact--mobile">917-555-4862</p>
  <p class="contact contact--office">516-555-7104</p>
  <p class="contact contact--fax">866-555-3927</p>
  <p class="contact contact--small contact--email">info@brightparcelroute.example</p>
  <p class="contact contact--web">brightparcelroute.example</p>
</div>
</body>
</html>
```